New Business Card Design Project

We are looking for a talented individual to create a truly awesome/unique business card design for us. We are looking for a someone to design something that will really stand out from the crowd - we don't mind what ideas you come up with (ie embossed/flat/matte/shine etc etc) just wow us with your creativity.
Updates

Target Market(s)

Video Games Industry Professionals (all levels of seniority from QA Testers through to CEOs)

Contact Information for Business Card

Company logo (see upload)
Company name: Northbay Play Careers Ltd
Employee Name: Darren Elsby
Job title: CEO
Website: www.nbpc2go.example
Office +44 1632 960418
Mobile: +44 7700 900276
Email: darren@nbpc2go.example

Colors

Designer to choose colors to be used in the design.

Requirements
Must have
• The business card design MUST contain all the information listed in the BUSINESS CARD DETAILS box.
• You will see the colours that are relevant to us (ie company logo) in the uploaded imagery - however you do not have to use all these colours when designing the business card itself
• MUST BE DOUBLE SIDED

```html
<!DOCTYPE html>
<html lang="en">
<head>
<meta charset="utf-8">
<title>Northbay Play Careers – Business Card</title>
<link rel="stylesheet" href="https://fonts.googleapis.com/css2?family=Open+Sans:wght@300;400;600;700&display=swap">
<style>
  :root {
    --backdrop: #2b2b2d;
    --card: #fbfbfc;
    --card-shade: #eceef1;
    --navy: #1f2d5c;
    --slate: #7e88a6;
    --orange: #f07a16;
    --ink: #20284a;
  }
  * { margin: 0; padding: 0; box-sizing: border-box; }
  html, body {
    width: 1200px; height: 900px; overflow: hidden;
    background: var(--backdrop);
    font-family: "Open Sans", Arial, sans-serif;
  }
  .canvas { position: relative; width: 1200px; height: 900px; }

  .card {
    position: absolute;
    width: 680px; height: 390px;
    border-radius: 32px;
    background: linear-gradient(160deg, var(--card) 0%, var(--card) 55%, var(--card-shade) 100%);
    overflow: hidden;
  }
  .card--front { left: 380px; top: 40px; }
  .card--back  { left: 140px; top: 470px; }

  /* Front */
  .front-mascot {
    position: absolute; right: 0; top: 0; width: 440px; height: 390px;
  }
  .front-wordmark {
    position: absolute; left: 40px; top: 196px;
    font-weight: 700; font-size: 30px; line-height: 1.1;
    color: var(--navy); letter-spacing: 0.5px;
    white-space: nowrap;
  }

  /* Back */
  .person { position: absolute; left: 46px; top: 38px; }
  .person__first { font-weight: 300; font-size: 30px; color: var(--ink); letter-spacing: 1px; line-height: 1.1; }
  .person__last  { font-weight: 700; font-size: 26px; color: var(--ink); letter-spacing: 0.5px; line-height: 1.1;
                   padding-bottom: 4px; border-bottom: 2px solid var(--orange); display: inline-block; }
  .person__role  { font-size: 15px; color: var(--orange); margin-top: 2px; letter-spacing: 0.5px; }

  .contact { position: absolute; left: 46px; top: 222px; list-style: none; }
  .contact__item { display: flex; align-items: center; gap: 12px; font-size: 18px; color: var(--ink); height: 30px; white-space: nowrap; }
  .contact__item svg { width: 18px; height: 18px; fill: var(--orange); flex: none; }
  .contact__web { position: absolute; left: 46px; top: 326px; font-size: 18px; color: var(--orange); white-space: nowrap; }

  .back-wordmark {
    position: absolute; right: 30px; top: 30px; height: 180px;
    writing-mode: vertical-rl; transform: rotate(180deg);
    font-weight: 700; font-size: 22px; color: var(--navy); line-height: 1.15;
    white-space: nowrap; text-align: start;
  }
  .back-mascot {
    position: absolute; right: 26px; bottom: 24px; width: 110px; height: 140px; border-radius: 14px;
  }
</style>
</head>
<body>
<main class="canvas">

  <section class="card card--front" aria-label="Business card front">
    <svg class="front-mascot" viewBox="0 0 440 390" role="img" aria-label="Mascot illustration: horned warrior with a long beard streaming to the left">
      <defs>
        <linearGradient id="mascotTone" x1="0" y1="0" x2="1" y2="0">
          <stop offset="0" stop-color="#7e88a6" stop-opacity="0.15"/>
          <stop offset="0.45" stop-color="#7e88a6" stop-opacity="0.7"/>
          <stop offset="1" stop-color="#1f2d5c"/>
        </linearGradient>
      </defs>
      <rect x="0" y="0" width="440" height="390" fill="url(#mascotTone)"/>
    </svg>
    <div class="front-wordmark">Northbay Play<br>Careers</div>
  </section>

  <section class="card card--back" aria-label="Business card back">
    <div class="person">
      <div class="person__first">DARREN</div>
      <div class="person__last">ELSBY</div>
      <div class="person__role">C.E.O.</div>
    </div>

    <ul class="contact">
      <li class="contact__item">
        <svg viewBox="0 0 24 24" aria-hidden="true"><path d="M3 9c0-3 4-5 9-5s9 2 9 5l-1 2-4-1V8c-2-.7-6-.7-8 0v2l-4 1zM6 12h12l2 8H4z"/></svg>
        +44 1632 960418
      </li>
      <li class="contact__item">
        <svg viewBox="0 0 24 24" aria-hidden="true"><path d="M7 2h10a1 1 0 0 1 1 1v18a1 1 0 0 1-1 1H7a1 1 0 0 1-1-1V3a1 1 0 0 1 1-1zm1 3v13h8V5zm4 14.5a1 1 0 1 0 0 .01z"/></svg>
        +44 7700 900276
      </li>
      <li class="contact__item">
        <svg viewBox="0 0 24 24" aria-hidden="true"><path d="M2 5h20v14H2zm2 2v.5l8 5.5 8-5.5V7zm0 3v7h16v-7l-8 5.5z"/></svg>
        darren@nbpc2go.example
      </li>
    </ul>
    <div class="contact__web">www.nbpc2go.example</div>

    <div class="back-wordmark">Northbay Play<br>Careers</div>
    <svg class="back-mascot" viewBox="0 0 110 140" role="img" aria-label="Small mascot illustration: horned bearded warrior">
      <rect width="110" height="140" rx="14" fill="#2e3c6b"/>
    </svg>
  </section>

</main>
</body>
</html>
```